Ward Compass Business Card Design*

We need a business card design for our company Ward Compass. Our company is specialized in providing online consulting services regarding medical institutions, hospitals and doctors. We work with patients worldwide looking to choose between healthcare providers. We have a website you may use as a reference, where we list doctors and clinics worldwide. So we target Medical providers as well as patients worldwide.
Target Market(s)
Medical Providers and patients around the world
Industry/Entity Type
Medical
Contact Information for Business Card
Salma Driouch
CEO
+90 612 348 2751
info@wardcompass.example
www.wardcompass.example
17 Essafsaf 3 H.Q.L. Rabat, Morocco
Requirements
Must have
- Company logo/name on one full side, personal info and smaller logo and company name on the other side.
Nice to have
- Smart and elegant design

```html
<!DOCTYPE html>
<html lang="en">
<head>
<meta charset="utf-8">
<title>Ward Compass — Business Card</title>
<link rel="stylesheet" href="https://fonts.googleapis.com/css2?family=Montserrat:wght@400;500;600;700&display=swap">
<style>
  :root {
    --page-bg: #e4e5e7;
    --card-bg: #f7f7f8;
    --card-edge: #c9cacd;
    --navy: #1b2a4a;
    --ink: #2a2f3a;
    --grey-mark: #9ea1a8;
    --map-tone: #dcdee2;
  }
  * { margin: 0; padding: 0; box-sizing: border-box; }
  html, body {
    width: 1200px; height: 970px; overflow: hidden;
    background: var(--page-bg);
    font-family: "Montserrat", sans-serif;
  }
  .card {
    position: absolute; left: 100px; top: 207px;
    width: 1000px; height: 556px;
    background: var(--card-bg);
    border: 1px solid var(--card-edge);
    box-shadow: 0 10px 30px rgba(0,0,0,0.08);
  }
  .world-map {
    position: absolute; left: 143px; top: 56px;
    width: 757px; height: 451px;
    background: radial-gradient(ellipse at 55% 45%, var(--map-tone) 0%, rgba(220,222,226,0.55) 55%, rgba(220,222,226,0) 80%);
  }
  .brand {
    position: absolute; left: 74px; top: 100px;
    display: flex; align-items: center; gap: 22px;
  }
  .brand-dot {
    width: 96px; height: 96px; border-radius: 50%;
    background: var(--navy);
  }
  .brand-name {
    font-size: 34px; font-weight: 600; letter-spacing: 1px;
    color: var(--navy); text-transform: uppercase;
  }
  .person {
    position: absolute; right: 72px; top: 278px; text-align: right;
  }
  .person-name { font-size: 32px; font-weight: 600; color: var(--navy); line-height: 1; }
  .divider {
    position: absolute; left: 74px; top: 330px;
    width: 783px; height: 2px; background: var(--navy);
  }
  .person-role {
    position: absolute; right: 72px; top: 320px;
    font-size: 19px; font-weight: 500; color: var(--ink);
  }
  .contacts {
    position: absolute; left: 74px; top: 358px;
    list-style: none; font-size: 22px; color: var(--ink);
  }
  .contacts li { display: flex; align-items: center; gap: 8px; height: 31px; }
  .contacts svg { width: 20px; height: 20px; fill: var(--navy); flex: none; }
  .address {
    position: absolute; right: 72px; top: 420px;
    font-style: normal; text-align: right;
    font-size: 22px; color: var(--ink); line-height: 31px;
  }
</style>
</head>
<body>
  <main class="card">
    <div class="world-map" role="img" aria-label="Faint world map spread across the card"></div>

    <div class="brand">
      <span class="brand-dot"></span>
      <span class="brand-name">Ward Compass</span>
    </div>

    <div class="person"><p class="person-name">Salma Driouch</p></div>
    <div class="divider"></div>
    <p class="person-role">CEO</p>

    <ul class="contacts">
      <li>
        <svg viewBox="0 0 24 24" aria-hidden="true"><path d="M3 8c0-3 4-5 9-5s9 2 9 5v2h-5V8H8v2H3zM6 12h12l3 8H3z"/></svg>
        +90 612 348 2751
      </li>
      <li>
        <svg viewBox="0 0 24 24" aria-hidden="true"><path d="M6 3h12v5H6zM3 9h18v8h-3v4H6v-4H3zm5 5v5h8v-5z"/></svg>
        +90 612 348 2751
      </li>
      <li>
        <svg viewBox="0 0 24 24" aria-hidden="true"><path d="M2 5h20v14H2zm2 2v.5l8 5.5 8-5.5V7z"/></svg>
        info@wardcompass.example
      </li>
      <li>
        <svg viewBox="0 0 24 24" aria-hidden="true"><path d="M12 2a10 10 0 1 0 0 20 10 10 0 0 0 0-20zm0 2a8 8 0 0 1 7.7 6H15c-.2-2-1-4-3-6zm-3 .6C8 6 7.4 8 7.3 10H4.3A8 8 0 0 1 9 4.6zM4.3 12h3c.1 2 .7 4 1.7 5.4A8 8 0 0 1 4.3 12zm5 0h5.4c-.2 2.4-1.2 4.6-2.7 6-1.5-1.4-2.5-3.6-2.7-6zm0-2c.2-2.4 1.2-4.6 2.7-6 1.5 1.4 2.5 3.6 2.7 6zM15 12h4.7A8 8 0 0 1 15 17.4c1-1.4 1.6-3.4 1.7-5.4z"/></svg>
        www.wardcompass.example
      </li>
    </ul>

    <address class="address">
      17 Essafsaf 3<br>
      H.Q.L. Rabat, Morocco
    </address>
  </main>
</body>
</html>
```